Business cards

Design business cards for our company. Just a straight, business like design with the logo, name, function and contact details

Target Market(s)

We are a innovative technological company active in water treatment

Industry/Entity Type

Water management

Contact Information for Business Card

Name, Function, email, telephone number, link to website

```html
<!DOCTYPE html>
<html lang="en">
<head>
<meta charset="utf-8">
<title>Aquarel9 Business Cards</title>
<link href="https://fonts.googleapis.com/css2?family=Open+Sans:wght@400;600;700&display=swap" rel="stylesheet">
<style>
  :root {
    --stage: #232324;
    --card-dark: #1f1f22;
    --card-grey: #a3a1a0;
    --accent: #2b95d6;
    --text-light: #f2f2f2;
    --text-muted: #a7a7a9;
    --deco-dark: #141416;
    --deco-mid: #2c2c30;
  }
  * { margin: 0; padding: 0; box-sizing: border-box; }
  html, body { width: 1200px; height: 780px; overflow: hidden; }
  body {
    background: var(--stage);
    font-family: "Open Sans", Arial, sans-serif;
    position: relative;
  }
  .card {
    position: absolute;
    top: 230px;
    width: 560px;
    height: 320px;
    overflow: hidden;
    box-shadow: 0 18px 40px rgba(0,0,0,.45);
  }
  .card--front { left: 30px; background: var(--card-dark); }
  .card--back { left: 610px; background: var(--card-grey); }

  .brand { position: absolute; left: 32px; top: 30px; display: flex; align-items: center; gap: 10px; }
  .brand__name { color: var(--accent); font-size: 34px; font-weight: 400; letter-spacing: .5px; line-height: 1; }
  .brand__mark { width: 30px; height: 30px; border-radius: 50%; background: var(--text-muted); }
  .brand__tagline { position: absolute; left: 34px; top: 70px; color: var(--text-muted); font-size: 9px; letter-spacing: 1.6px; }

  .address { position: absolute; left: 58px; top: 118px; color: var(--text-light); font-size: 15px; line-height: 22px; }
  .contact { position: absolute; left: 34px; top: 172px; list-style: none; color: var(--text-light); font-size: 15px; line-height: 23px; }
  .contact li { display: flex; align-items: center; gap: 8px; }
  .contact svg { width: 14px; height: 14px; flex: none; }

  .person { position: absolute; right: 36px; top: 188px; text-align: right; }
  .person__name { font-size: 30px; font-weight: 700; line-height: 1.1; color: var(--text-muted); }
  .person__first { color: var(--accent); }
  .person__role { color: var(--text-light); font-size: 18px; font-weight: 600; margin-top: 2px; }
  .accent-bar { position: absolute; right: 0; top: 196px; width: 14px; height: 60px; background: var(--accent); }

  .decoration {
    position: absolute; left: 250px; top: 230px; width: 200px; height: 110px;
    background: radial-gradient(ellipse at 50% 40%, var(--deco-mid), var(--deco-dark) 70%, transparent 72%);
  }

  .pattern { position: absolute; inset: 0; background: linear-gradient(135deg, #b2b0ae, #9a9897 55%, #a9a7a6); }
  .back-brand { position: absolute; right: 40px; bottom: 40px; display: flex; align-items: center; gap: 8px; }
  .back-brand__name { color: #ffffff; font-size: 20px; font-weight: 400; }
  .back-brand__mark { width: 16px; height: 16px; border-radius: 50%; background: #ffffff; }
</style>
</head>
<body>
  <section class="card card--front">
    <div class="brand">
      <span class="brand__name">Aquarel9</span>
      <span class="brand__mark"></span>
    </div>
    <div class="brand__tagline">NANOBUBBLE TECHNOLOGY</div>

    <address class="address" style="font-style:normal">
      1840 Lakeside Ave. Suite 310<br>
      Riverton, TX 75210
    </address>

    <ul class="contact">
      <li>
        <svg viewBox="0 0 16 16" aria-hidden="true"><path fill="#2b95d6" d="M3.6 1.5l2.3 2.6-1.3 1.6c.9 2 2.6 3.7 4.6 4.6l1.6-1.3 2.6 2.3-1.2 2.1C6.8 13.2 2.8 9.2 1.5 4.1z"/></svg>
        (555) 204-7319
      </li>
      <li>
        <svg viewBox="0 0 16 16" aria-hidden="true"><rect x="1" y="3.5" width="14" height="9" rx="1" fill="#2b95d6"/><path d="M1.5 4l6.5 5 6.5-5" stroke="#1f1f22" stroke-width="1.4" fill="none"/></svg>
        hello@aquarel9.example
      </li>
      <li>
        <svg viewBox="0 0 16 16" aria-hidden="true"><circle cx="8" cy="8" r="6.5" fill="#2b95d6"/><path d="M1.5 8h13M8 1.5c-3 3.5-3 9.5 0 13M8 1.5c3 3.5 3 9.5 0 13" stroke="#1f1f22" stroke-width="1" fill="none"/></svg>
        www.aquarel9.example
      </li>
    </ul>

    <div class="decoration" role="img" aria-label="Large embossed brand symbol decoration area"></div>

    <div class="person">
      <div class="person__name"><span class="person__first">Mirela</span> Hostova</div>
      <div class="person__role">Managing Director</div>
    </div>
    <div class="accent-bar"></div>
  </section>

  <section class="card card--back">
    <div class="pattern" role="img" aria-label="Repeating pattern of brand symbols in grey, black and white tones"></div>
    <div class="back-brand">
      <span class="back-brand__name">Aquarel9</span>
      <span class="back-brand__mark"></span>
    </div>
  </section>
</body>
</html>
```